Road Construction Company needs business cards

We would like a new business card designed for our business.

We're a road construction company based in Qld, Australia.

Can the business card please have the following information on it.

Name: Brent Malvoy
Position: General Manager
Phone: 0471 592 304
Email: Brent.malvoy@quendix.com.au
Address: 87 Harrowgate Ave, Pindarra, QLD, 4000
Website: www.quendix.com.au

Visually we'd like the card to be professional and simple.

Attached is our logo.

Our website is www.quendix.com.au

Target Market(s)

Men aged 25-60

Contact Information for Business Card

As listed in project description

Font styles to use
Serif

Requirements
Must have
• Large logo on back of card

```html
<!DOCTYPE html>
<html lang="en">
<head>
<meta charset="utf-8">
<title>Quendix Business Card</title>
<link href="https://fonts.googleapis.com/css2?family=Poppins:wght@300;400;600;700&family=Roboto+Condensed:wght@500&display=swap" rel="stylesheet">
<style>
  :root {
    --page-bg: #d9d9d9;
    --card-bg: #0a0e11;
    --accent: #3fcbe9;
    --ink-light: #ffffff;
    --ink-soft: #e6e6e6;
  }
  * { box-sizing: border-box; margin: 0; padding: 0; }
  html, body {
    width: 1200px; height: 846px; overflow: hidden;
    background: var(--page-bg);
  }
  .canvas { position: relative; width: 1200px; height: 846px; }
  .card {
    position: absolute; left: 347px; width: 509px; height: 291px;
    background: var(--card-bg); overflow: hidden;
  }
  .card--front { top: 99px; }
  .card--back { top: 458px; display: flex; align-items: center; justify-content: center; }

  .wordmark {
    font-family: "Poppins", sans-serif; font-weight: 700;
    color: var(--ink-light); letter-spacing: 0.04em; line-height: 1;
  }
  .card--front .wordmark { position: absolute; left: 37px; top: 34px; font-size: 32px; }
  .card--back .wordmark { font-size: 58px; }

  .machine-photo {
    position: absolute; right: 0; top: 0; width: 240px; height: 291px;
    background: radial-gradient(ellipse at 55% 50%, #2b3033 0%, #15191c 45%, var(--card-bg) 75%);
  }

  .person-name {
    position: absolute; left: 37px; top: 92px;
    font-family: "Poppins", sans-serif; font-weight: 600;
    font-size: 20px; color: var(--accent); letter-spacing: -0.01em;
  }
  .person-role {
    position: absolute; left: 37px; top: 120px;
    font-family: "Poppins", sans-serif; font-weight: 300;
    font-size: 12px; color: var(--ink-soft);
  }

  .contact-list { position: absolute; left: 36px; top: 150px; list-style: none; }
  .contact-item {
    display: flex; align-items: flex-start; gap: 9px;
    font-family: "Roboto Condensed", sans-serif; font-weight: 500;
    font-size: 15px; line-height: 18px; color: var(--ink-light);
    margin-bottom: 4px;
  }
  .contact-icon { width: 19px; height: 18px; flex: none; fill: var(--accent); }
  .contact-item--address .contact-icon { height: 32px; }
</style>
</head>
<body>
<main class="canvas">
  <section class="card card--front">
    <div class="wordmark">QUENDIX</div>
    <div class="machine-photo" role="img" aria-label="Dark studio photo of a road roller compactor"></div>
    <h1 class="person-name">Brent Malvoy</h1>
    <p class="person-role">General Manager</p>
    <ul class="contact-list">
      <li class="contact-item">
        <svg class="contact-icon" viewBox="0 0 24 24"><path d="M6.6 2.5l3 3.2-1.8 2.6c.9 2.6 3 5.4 5.5 7.1l2.5-1.6 3.2 3-1.6 3.4C10 20 4 13.5 3.4 4.3z"/></svg>
        <span>0471 592 304</span>
      </li>
      <li class="contact-item">
        <svg class="contact-icon" viewBox="0 0 24 18"><path d="M1 2h22v1.5L12 10 1 3.5z"/><path d="M1 6l11 6.5L23 6v11H1z"/></svg>
        <span>Brent.malvoy@quendix.com.au</span>
      </li>
      <li class="contact-item contact-item--address">
        <svg class="contact-icon" viewBox="0 0 20 32"><path d="M10 1a9 9 0 0 0-9 9c0 7 9 21 9 21s9-14 9-21a9 9 0 0 0-9-9zm0 5a4 4 0 1 1 0 8 4 4 0 0 1 0-8z" fill-rule="evenodd"/></svg>
        <span>87 Harrowgate Ave, Pindarra,<br>QLD, 4000</span>
      </li>
      <li class="contact-item">
        <svg class="contact-icon" viewBox="0 0 24 24"><circle cx="12" cy="12" r="10.5" fill="none" stroke="#3fcbe9" stroke-width="1.8"/><ellipse cx="12" cy="12" rx="4.5" ry="10.5" fill="none" stroke="#3fcbe9" stroke-width="1.6"/><path d="M1.5 12h21M3.5 7h17M3.5 17h17" stroke="#3fcbe9" stroke-width="1.6"/></svg>
        <span>www.quendix.com.au</span>
      </li>
    </ul>
  </section>

  <section class="card card--back">
    <div class="wordmark">QUENDIX</div>
  </section>
</main>
</body>
</html>
```